Commercial janitorial cleaning

Janitorial cleaning particularly for commercial buildings. Website needs to specify free estimates. Location of service is Hudson, Valatie, East Greenbush, Troy, Albany ny area. Services page with Janitorial services- General Office Cleaning, Construction Cleaning, Carpet Extraction, Consultation/Business, Lighting Maintenance, Seasonal Deep Cleaning, Window cleaning, Event Cleaning, Floor and Carpet Cleaning, Floor Striping and Waxing. Contact us page with email phone number on page and a request page that emails me if they have any questions. About us page-the picture of my family on it with a section I can type a story myself.

Target Market(s)

Commercial businesses

Industry/Entity Type

Janitorial Service

Number of Pages Required

4 page

Font styles to use
Serif
Sans Serif
Script

Colors
ec1f27
1b1b1b
ffffff
9d9d9d

Requirements
Must have
• Phone number 555-304-7162. Must have free estimates on home page. Going for industrial / modern look to website
Nice to have
• Logo is a red and black building so if those colors could be coordinated to website that would be awesome.

```html
<!DOCTYPE html>
<html lang="en">
<head>
<meta charset="utf-8">
<title>Brightline Cleaning Services</title>
<link href="https://fonts.googleapis.com/css2?family=Raleway:wght@300;400;500;600;700;800&family=Open+Sans:wght@400;600;700&display=swap" rel="stylesheet">
<style>
:root{
  --red:#ec1f27;
  --ink:#1b1b1b;
  --white:#ffffff;
  --grey:#9d9d9d;
  --panel:#8f8f8f;
  --light:#ececec;
  --text:#555555;
}
*{box-sizing:border-box;margin:0;padding:0}
html,body{width:1200px;height:3056px;overflow:hidden;background:var(--white)}
body{position:relative;font-family:"Open Sans",Arial,sans-serif;color:var(--text)}
.abs{position:absolute}

/* header / hero */
.hero{left:0;top:0;width:1200px;height:560px;background:linear-gradient(180deg,#2a2a2a 0%,#4a4a4a 45%,#1f1f1f 100%)}
.brand{display:flex;align-items:center;gap:8px;font-family:"Raleway",sans-serif;font-weight:700;color:var(--white);white-space:nowrap}
.brand-mark{width:28px;height:28px;background:var(--red);flex:none}
.header-brand{left:170px;top:18px;font-size:13px;letter-spacing:.5px}
.nav{left:318px;top:24px;display:flex;gap:30px;font-family:"Raleway",sans-serif;font-weight:700;font-size:14px;color:var(--white);white-space:nowrap}
.call{left:712px;top:16px;display:flex;align-items:center;gap:8px;color:var(--white);font-family:"Raleway",sans-serif;white-space:nowrap}
.call small{display:block;font-size:11px;font-weight:700}
.call strong{display:block;font-size:19px;font-weight:700;line-height:1}
.quote-btn{background:var(--red);color:var(--white);font-family:"Raleway",sans-serif;font-weight:800;text-align:center;line-height:1;border-radius:3px}
.hero-title{left:0;width:1200px;top:232px;text-align:center;color:var(--white)}
.hero-title .l1{font-family:"Raleway",sans-serif;font-weight:300;font-size:30px}
.hero-title .l2{font-family:"Raleway",sans-serif;font-weight:400;font-size:46px;line-height:1.1}

/* welcome */
.welcome{left:170px;top:510px;width:858px;height:520px;background:var(--white)}
.family-photo{left:8px;top:5px;width:340px;height:470px;background:linear-gradient(160deg,#5c7a3a,#9a8c6e 55%,#4a5a6a)}
.welcome-text{left:365px;top:30px;width:470px;text-align:center}
.eyebrow{font-family:"Raleway",sans-serif;font-size:15px;color:#6a6a6a;font-weight:500;letter-spacing:.5px}
.red-title{font-family:"Raleway",sans-serif;color:var(--red);font-weight:500}
.rule{height:1px;background:#cfcfcf;margin:8px auto 0;position:relative}
.rule:after{content:"";position:absolute;left:50%;top:-1px;width:80px;height:3px;margin-left:-40px;background:var(--red)}
.welcome p{font-size:12.5px;line-height:22px;color:#666;margin-top:18px}
.outline-btn{display:inline-block;border:1px solid #999;font-size:11px;color:#777;padding:10px 30px;font-family:"Raleway",sans-serif}

/* services */
.services{left:0;top:1030px;width:1200px;height:435px;background:linear-gradient(180deg,#2b2b2b,#1b1b1b)}
.section-head{left:0;width:1200px;text-align:center}
.section-head .eyebrow{color:#cfcfcf}
.service-card{top:133px;width:278px;height:160px}
.service-photo{width:100%;height:100%}
.service-label{position:absolute;left:-10px;right:-10px;bottom:-34px;height:38px;line-height:38px;text-align:center;color:var(--white);font-family:"Raleway",sans-serif;font-size:19px;background:var(--red);clip-path:polygon(2% 0,100% 0,98% 100%,0 100%)}
.services .outline-btn{border-color:#9d9d9d;color:#ccc}

/* why choose */
.why{left:172px;top:1508px;width:856px;height:254px;background:var(--grey)}
.why-lead{left:0;top:0;width:283px;height:254px;background:var(--red);color:var(--white);font-family:"Raleway",sans-serif;font-weight:700;font-size:26px;line-height:28px;text-align:right;padding:24px 28px 0 0}
.feature{width:272px;height:112px;background:var(--panel);border:1px solid #a8a8a8;color:var(--white);padding:14px 8px 0 56px}
.feature h4{font-family:"Raleway",sans-serif;font-weight:600;font-size:11.5px;text-transform:uppercase;white-space:nowrap}
.feature p{font-size:11px;line-height:17px;margin-top:12px}
.feature svg{position:absolute;left:16px;top:30px}

/* testimonials */
.testi{left:0;top:1820px;width:1200px;height:565px}
.testi-bg{left:0;top:0;width:1200px;height:565px;background:linear-gradient(180deg,#3a3a3a,#262626 50%,#333)}
.t-card{top:175px;width:268px;height:230px;background:var(--white);border-radius:4px;text-align:center;padding:22px 18px 0}
.t-card:after{content:"";position:absolute;left:50%;bottom:-12px;margin-left:-12px;border:12px solid transparent;border-bottom:0;border-top-color:var(--white)}
.t-card p{font-size:11px;line-height:16px;font-style:italic;color:#555}
.stars{color:var(--red);font-size:14px;letter-spacing:2px;margin-top:12px}
.t-card h5{font-size:12px;color:#222;margin-top:6px}
.t-card span{font-size:11px;color:#777}
.avatar{top:436px;width:70px;height:70px;border-radius:50%;background:linear-gradient(#d8d8d8,#9a9a9a);border:3px solid var(--white)}

/* info boxes */
.info{background:var(--light);padding:26px 22px}
.info h3{font-family:"Raleway",sans-serif;color:var(--red);font-weight:700;font-size:19px;line-height:24px}
.info p{font-size:12px;line-height:20px;color:#666;margin-top:16px}

/* footer */
.footer{left:0;top:2795px;width:1200px;height:261px;background:var(--ink);color:#bbb}
.notch{left:550px;top:2770px;width:100px;height:26px;background:var(--ink);border-radius:50px 50px 0 0}
.f-col h6{font-family:"Raleway",sans-serif;color:var(--white);font-size:12px;font-weight:700;text-transform:uppercase;margin-bottom:14px}
.f-col li{list-style:none;font-size:12px;line-height:18px}
.f-col p{font-size:12px;line-height:18px}
.newsletter{display:flex;margin-top:14px}
.newsletter span{width:190px;height:34px;background:var(--white);color:#777;font-size:11px;padding:10px}
.newsletter b{width:85px;height:34px;background:var(--red);color:var(--white);font-size:11px;text-align:center;line-height:34px}
.social{display:flex;gap:14px;margin-top:8px}
.social i{width:22px;height:22px;border:2px solid #777;border-radius:50%}
.copyright{left:172px;top:3005px;font-size:11px;color:#888}
</style>
</head>
<body>

<!-- hero -->
<section class="abs hero" role="img" aria-label="Black and white photo of a modern glass office building"></section>
<div class="abs brand header-brand"><span class="brand-mark"></span>BRIGHTLINE</div>
<nav class="abs nav"><span>HOME</span><span>ABOUT US</span><span>SERVICES</span><span>CONTACT US</span></nav>
<div class="abs call">
  <svg width="28" height="28" viewBox="0 0 24 24"><path fill="#fff" d="M6.6 10.8a15.1 15.1 0 0 0 6.6 6.6l2.2-2.2c.3-.3.7-.4 1-.2 1.1.4 2.3.6 3.6.6.6 0 1 .4 1 1V20c0 .6-.4 1-1 1A17 17 0 0 1 3 4c0-.6.4-1 1-1h3.5c.6 0 1 .4 1 1 0 1.3.2 2.5.6 3.6.1.3 0 .7-.2 1z"/></svg>
  <div><small>CALL US</small><strong>555-304-7162</strong></div>
</div>
<div class="abs quote-btn" style="left:893px;top:9px;width:120px;height:48px;padding-top:7px;font-size:17px">GET A<br>FREE QUOTE</div>
<div class="abs hero-title"><div class="l1">Janitorial Cleaning Particularly for</div><div class="l2">Commercial Buildings</div></div>

<!-- welcome -->
<section class="abs welcome">
  <div class="abs family-photo" role="img" aria-label="Family photo of the owners on a ladder in an orchard"></div>
  <div class="abs welcome-text">
    <div class="eyebrow">WELCOME TO</div>
    <h2 class="red-title" style="font-size:26px">Brightline Cleaning Services</h2>
    <div class="rule" style="width:360px"></div>
    <p>Lorem ipsum dolor sit amet, consectetur adipiscing elit, sed do eiusmod tempor incididunt ut labore et dolore magna aliqua. Ut enim ad minim veniam, quis nostrud exercitation ullamco laboris nisi ut aliquip ex ea commodo consequat. Duis aute irure dolor in reprehenderit in voluptate velit esse cillum dolore eu fugiat nulla pariatur. Excepteur sint occaecat cupidatat non proident, sunt in culpa qui officia deserunt mollit anim id est laborum.</p>
    <p>Sed ut perspiciatis unde omnis iste natus error sit voluptatem accusantium doloremque laudantium, totam rem aperiam, eaque ipsa quae ab illo inventore veritatis et quasi architecto beatae vitae dicta sunt explicabo. Nemo enim ipsam voluptatem quia voluptas sit aspernatur aut odit aut fugit, sed quia consequuntur magni dolores eos qui ratione voluptatem sequi nesciunt. Neque porro quisquam est, qui dolorem</p>
    <div style="margin-top:18px"><span class="outline-btn">READ MORE</span></div>
  </div>
</section>

<!-- services -->
<section class="abs services" role="img" aria-label="Dark faded background photo of an office building">
  <div class="abs section-head" style="top:40px">
    <div class="eyebrow">OUR SERVICES</div>
    <h2 class="red-title" style="font-size:26px;font-weight:600">What We Do</h2>
    <div class="rule" style="width:290px;background:#666"></div>
  </div>
  <div class="abs service-card" style="left:183px"><div class="service-photo" role="img" aria-label="Yellow mop bucket and wet floor sign" style="background:linear-gradient(135deg,#d8c24a,#7a6f3a 60%,#3b3b3b)"></div><div class="service-label">Janitorial Services</div></div>
  <div class="abs service-card" style="left:462px"><div class="service-photo" role="img" aria-label="Cleaners working in an office" style="background:linear-gradient(135deg,#7b8c9a,#c9d2d8 55%,#5a6670)"></div><div class="service-label">General Office Cleaning</div></div>
  <div class="abs service-card" style="left:741px"><div class="service-photo" role="img" aria-label="Worker cleaning a construction site floor" style="background:linear-gradient(135deg,#b9c2c8,#8b8f92 55%,#d07a2a)"></div><div class="service-label">Construction Cleaning</div></div>
  <div class="abs" style="left:0;width:1200px;top:353px;text-align:center"><span class="outline-btn">VIEW MORE</span></div>
</section>

<!-- why choose -->
<section class="abs why">
  <div class="abs why-lead">Why Choose<br>Brightline<br>Cleaning Services</div>
  <div class="abs feature" style="left:292px;top:6px">
    <svg width="26" height="26" viewBox="0 0 26 26"><circle cx="13" cy="13" r="9" fill="none" stroke="#fff" stroke-width="2"/><circle cx="13" cy="13" r="3" fill="#fff"/></svg>
    <h4>Quality</h4><p>Lorem ipsum dolor sit amet, conse ctetur adipiscing elit, sed do eiusmod tempor incididunt.</p></div>
  <div class="abs feature" style="left:574px;top:6px">
    <svg width="26" height="26" viewBox="0 0 26 26"><circle cx="9" cy="15" r="6" fill="none" stroke="#fff" stroke-width="2"/><circle cx="19" cy="8" r="4" fill="none" stroke="#fff" stroke-width="2"/></svg>
    <h4>Services</h4><p>Lorem ipsum dolor sit amet, conse ctetur adipiscing elit, sed do eiusmod tempor incididunt.</p></div>
  <div class="abs feature" style="left:292px;top:126px">
    <svg width="26" height="26" viewBox="0 0 26 26"><path d="M13 2l9 4v6c0 6-4 10-9 12-5-2-9-6-9-12V6z" fill="none" stroke="#fff" stroke-width="2"/><path d="M8 13l4 4 6-7" fill="none" stroke="#fff" stroke-width="2"/></svg>
    <h4>Responsible and Trustworthy</h4><p>Lorem ipsum dolor sit amet, conse ctetur adipiscing elit, sed do eiusmod tempor incididunt.</p></div>
  <div class="abs feature" style="left:574px;top:126px">
    <svg width="26" height="26" viewBox="0 0 26 26"><circle cx="13" cy="10" r="7" fill="none" stroke="#fff" stroke-width="2"/><path d="M9 16l-2 8 6-3 6 3-2-8" fill="none" stroke="#fff" stroke-width="2"/></svg>
    <h4>Certified Green Company</h4><p>Lorem ipsum dolor sit amet, conse ctetur adipiscing elit, sed do eiusmod tempor incididunt.</p></div>
</section>

<!-- testimonials -->
<section class="abs testi">
  <div class="abs testi-bg" role="img" aria-label="Grayscale mosaic of customer portrait photos"></div>
  <svg class="abs" style="left:0;top:0" width="1200" height="565" viewBox="0 0 1200 565">
    <polygon points="0,0 1200,0 1200,0 0,22" fill="#fff"/>
    <polygon points="700,22 1200,0 1200,34" fill="#ec1f27"/>
    <polygon points="0,530 520,565 0,565" fill="#ec1f27"/>
    <polygon points="0,548 1200,565 1200,585 0,585" fill="#fff"/>
  </svg>
  <div class="abs section-head" style="top:78px">
    <div class="eyebrow" style="color:#ddd">TESTIMONIALS</div>
    <h2 class="red-title" style="font-size:27px;font-weight:600"><span style="display:inline-block;width:26px;height:26px;border-radius:50%;background:var(--red);color:#fff;font-size:20px;line-height:30px;vertical-align:3px;margin-right:10px">&ldquo;</span>Happy Customers</h2>
    <div class="rule" style="width:300px;background:#777"></div>
  </div>
  <div class="abs t-card" style="left:174px"><p>"Lorem ipsum dolor sit amet, consectetur adipiscing elit, sed do eiusmod tempor incididunt ut labore et dolore magna aliqua. Ut enim ad minim veniam, quis nostrud exercitation ullamco laboris nisi ut aliquip ex ea commodo consequat. Duis aute irure dolor in reprehenderit in voluptate velit esse."</p><div class="stars">★★★★★</div><h5>John Doe</h5><span>Lorem ipsum dolor</span></div>
  <div class="abs t-card" style="left:466px"><p>"Lorem ipsum dolor sit amet, consectetur adipiscing elit, sed do eiusmod tempor incididunt ut labore et dolore magna aliqua. Ut enim ad minim veniam, quis nostrud exercitation ullamco laboris nisi ut aliquip ex ea commodo consequat. Duis aute irure dolor in reprehenderit in voluptate velit esse."</p><div class="stars">★★★★★</div><h5>John Doe</h5><span>Lorem ipsum dolor</span></div>
  <div class="abs t-card" style="left:757px"><p>"Lorem ipsum dolor sit amet, consectetur adipiscing elit, sed do eiusmod tempor incididunt ut labore et dolore magna aliqua. Ut enim ad minim veniam, quis nostrud exercitation ullamco laboris nisi ut aliquip ex ea commodo consequat. Duis aute irure dolor in reprehenderit in voluptate velit esse."</p><div class="stars">★★★★★</div><h5>John Doe</h5><span>Lorem ipsum dolor</span></div>
  <div class="abs avatar" style="left:273px" role="img" aria-label="Customer portrait"></div>
  <div class="abs avatar" style="left:565px" role="img" aria-label="Customer portrait"></div>
  <div class="abs avatar" style="left:856px" role="img" aria-label="Customer portrait"></div>
</section>

<!-- info boxes -->
<div class="abs info" style="left:172px;top:2405px;width:268px;height:335px"><h3>What services does your company require?</h3><p>Lorem ipsum dolor sit amet, consectetur adipiscing elit, sed do eiusmod tempor incididunt ut labore et dolore magna aliqua. Ut enim ad minim veniam, quis nostrud exercitation ullamco laboris nisi ut aliquip ex ea commodo consequat.</p></div>
<div class="abs info" style="left:465px;top:2425px;width:262px;height:285px"><h3>Let us clean for you!</h3><p>Lorem ipsum dolor sit amet, consectetur adipiscing elit, sed do eiusmod tempor incididunt ut labore et dolore magna aliqua. Ut enim ad minim veniam, quis nostrud exercitation ullamco laboris nisi ut aliquip ex ea commodo consequat. Duis aute irure dolor in reprehenderit.</p></div>
<div class="abs info" style="left:742px;top:2490px;width:270px;height:240px;padding-top:22px"><h3>Why do Companies trust us?</h3><p style="margin-top:12px">Lorem ipsum dolor sit amet, consectetur adipiscing elit, sed do eiusmod tempor incididunt ut labore et dolore magna aliqua. Ut enim ad minim veniam, quis nostrud exercitation ullamco laboris nisi ut aliquip ex ea commodo consequat.</p></div>

<!-- footer -->
<div class="abs notch"></div>
<svg class="abs" style="left:590px;top:2776px" width="20" height="18" viewBox="0 0 20 18"><path d="M10 2v14M4 8l6-6 6 6" fill="none" stroke="#fff" stroke-width="2"/></svg>
<footer class="abs footer">
  <div class="abs brand" style="left:172px;top:34px;font-size:15px"><span class="brand-mark"></span>BRIGHTLINE</div>
  <div class="abs quote-btn" style="left:172px;top:130px;width:120px;height:48px;padding-top:7px;font-size:17px">GET A<br>FREE QUOTE</div>
  <div class="abs f-col" style="left:404px;top:28px"><h6>Quick Links</h6><ul><li>Home</li><li>About Us</li><li>Services</li><li>Contact Us</li></ul></div>
  <div class="abs f-col" style="left:538px;top:28px"><h6>Contact Us</h6><p>Your Company LTD.<br>Street Name, 000000,<br>City Name</p>
    <p style="color:#fff;font-weight:700;margin-top:12px">Phone</p><p style="font-size:19px;color:#ddd">555-304-7162</p>
    <p style="color:#fff;font-weight:700;margin-top:10px">Email</p><p>hello@brightlinecleaning.example</p></div>
  <div class="abs f-col" style="left:757px;top:28px;width:275px"><h6>Newsletter Subscribe</h6><p>Enter your email address below and get the latest</p>
    <div class="newsletter"><span>Enter your Email Id here...</span><b>SUBSCRIBE</b></div>
    <h6 style="margin-top:24px;margin-bottom:4px">Get Connect With Us</h6>
    <div class="social"><i></i><i></i><i></i><i></i></div></div>
</footer>
<div class="abs copyright">© 2017 Brightline Cleaning Services. All Rights Reserved</div>

</body>
</html>
```